Website for Accounting firm for dental practices

We need a website for our accounting firm for Dentists. We want it to be three pages, a HOME, SERVICES, and CONTACT US page. The logo for the firm is attached. Also attached is the wording we are going to use in the website. We would like the colors to go with the logo (the color logo). We want this page to look professional when people come to the page.

Industry/Entity Type

Accounting

Coding

Coded - Design and coding required

Number of Pages Required

1 page

```html
<!DOCTYPE html>
<html lang="en">
<head>
<meta charset="utf-8">
<title>BrightLedger Dental</title>
<link rel="stylesheet" href="https://fonts.googleapis.com/css2?family=Raleway:wght@400;500;600;700&display=swap">
<style>
:root{
  --blue:#2aa7e1;
  --blue-dark:#1b8fc8;
  --blue-deep:#137fb8;
  --ink:#333a40;
  --grey:#8a9096;
  --line:#e3e7ea;
  --white:#ffffff;
  --pale:#eaf6fc;
}
*{box-sizing:border-box;margin:0;padding:0}
html,body{width:1200px;height:2416px;overflow:hidden}
body{font-family:"Raleway",sans-serif;color:var(--ink);background:var(--white);position:relative}
.wrap{position:absolute;left:172px;width:856px}

/* header */
.site-header{position:absolute;top:0;left:0;width:1200px;height:70px;background:var(--white)}
.brand{position:absolute;left:166px;top:10px;color:var(--blue);font-weight:700;font-size:20px;line-height:24px}
.main-nav{position:absolute;right:172px;top:0;height:70px;display:flex;align-items:center;font-size:12px;font-weight:600;letter-spacing:.5px}
.main-nav a{color:var(--ink);text-decoration:none;padding:0 12px;border-left:1px solid var(--line)}
.main-nav a:first-child{border-left:0}
.main-nav a.active{color:var(--blue)}
.main-nav .call{color:var(--blue);font-weight:700;padding-right:0}

/* hero */
.hero{position:absolute;top:70px;left:0;width:1200px;height:486px;background:linear-gradient(100deg,#bfe3f3 0%,#d8eef8 30%,#e9d6cc 55%,#f3e1d6 70%,#3f6fb8 88%,#d7ecf6 100%)}
.hero-card{position:absolute;left:172px;width:330px;height:118px;background:rgba(255,255,255,.93);display:flex;border:3px solid rgba(255,255,255,.7)}
.hero-card .thumb{width:124px;height:100%;flex:none}
.hero-card .body{padding:12px 14px;position:relative;flex:1}
.hero-card h3{color:var(--blue);font-size:15px;font-weight:600;margin-bottom:6px}
.hero-card p{font-size:10.5px;line-height:14px;color:var(--grey)}
.hero-card .go{position:absolute;right:0;bottom:0;width:16px;height:16px;background:var(--blue)}
.hero-card .go svg{display:block}

/* services */
.services{top:556px;height:599px}
.service{position:absolute;width:340px;display:flex}
.service .icon{width:97px;height:97px;border-radius:50%;background:var(--blue);flex:none;display:flex;align-items:center;justify-content:center}
.service .text{padding-left:18px;padding-top:2px}
.service h3{color:var(--blue);font-size:16px;font-weight:600;margin-bottom:6px}
.service p{font-size:11px;line-height:15px;color:var(--grey)}
.service .more{display:inline-block;margin-top:2px;font-size:10.5px;color:var(--blue);text-decoration:underline}

.cta{position:absolute;left:0;top:416px;width:856px;height:81px;border:2px solid var(--line);box-shadow:0 2px 4px rgba(0,0,0,.08);display:flex;align-items:center;justify-content:space-between;padding:0 20px 0 20px}
.cta p{font-size:19px;font-weight:600;color:var(--ink)}
.cta .button{width:258px;height:42px;background:var(--blue);color:var(--white);font-size:12px;font-weight:600;letter-spacing:.5px;display:flex;align-items:center;justify-content:center}

/* financial band */
.finance{position:absolute;top:1155px;left:0;width:1200px;height:416px;overflow:hidden}
.finance .backdrop{position:absolute;inset:0;background:linear-gradient(90deg,#2b9fd9 0%,#47b2e6 35%,#3aa9e2 60%,#2b98d2 100%)}
.finance h2{position:absolute;top:62px;left:0;width:1200px;text-align:center;color:var(--white);font-size:19px;font-weight:600}
.finance ul{position:absolute;top:132px;list-style:none;color:var(--white);font-size:15.5px}
.finance li{height:39px;display:flex;align-items:flex-start}
.finance li::before{content:"";width:7px;height:7px;border-radius:50%;background:var(--white);margin:7px 14px 0 0;flex:none}
.finance .col-a{left:172px}
.finance .col-b{left:572px}

/* smiles */
.smiles{top:1571px;height:666px}
.smiles h2{position:absolute;top:68px;left:0;color:var(--blue);font-size:19px;font-weight:600}
.smile{position:absolute;width:271px}
.smile .photo{height:177px;border:5px solid var(--white);box-shadow:0 0 0 1px var(--line)}
.smile p{margin-top:12px;font-size:10.5px;line-height:15px;color:var(--grey)}

.appointment{position:absolute;left:582px;top:69px;width:274px;height:524px;border:1px solid var(--line)}
.appointment header{position:relative;height:84px;background:var(--blue);color:var(--white);text-align:center;padding-top:14px}
.appointment header::after{content:"";position:absolute;left:50%;bottom:-16px;margin-left:-18px;border-left:18px solid transparent;border-right:18px solid transparent;border-top:16px solid var(--blue)}
.appointment h3{font-size:18px;font-weight:600}
.appointment .phone{margin-top:8px;font-size:18px;font-weight:700;display:flex;align-items:center;justify-content:center;gap:8px}
.field{position:absolute;left:15px;width:244px;height:38px;border:1px solid var(--line);font-size:9.5px;color:var(--grey);letter-spacing:.5px;padding:13px 10px}
.submit{position:absolute;left:15px;top:462px;width:244px;height:38px;background:var(--blue);color:var(--white);font-size:11px;font-weight:600;display:flex;align-items:center;justify-content:center}

/* footer */
.site-footer{position:absolute;top:2237px;left:0;width:1200px;height:179px;background:var(--blue);color:var(--white)}
.contact{position:absolute;left:172px;top:58px}
.contact h4{font-size:16px;font-weight:600;margin-bottom:10px}
.contact p{font-size:12px;line-height:18px}
.divider{position:absolute;top:50px;width:1px;height:82px;background:rgba(255,255,255,.5)}
.footer-brand{position:absolute;left:452px;top:48px;width:200px;text-align:center;font-size:28px;font-weight:700;line-height:34px}
.social{position:absolute;left:733px;top:52px;display:flex;gap:12px}
.social span{width:36px;height:36px;border-radius:50%;background:var(--white)}
.copyright{position:absolute;left:733px;top:106px;font-size:11.5px}
</style>
</head>
<body>

<header class="site-header">
  <div class="brand">BrightLedger<br>Dental</div>
  <nav class="main-nav">
    <a class="active" href="#">HOME</a>
    <a href="#">ABOUT US</a>
    <a href="#">SERVICES</a>
    <a href="#">CONTACT US</a>
    <a class="call" href="#">CALL US : 555-014-2290</a>
  </nav>
</header>

<section class="hero" role="img" aria-label="Photo of a smiling patient in a dental chair with a dentist holding a mirror">
  <article class="hero-card" style="top:48px">
    <div class="thumb" role="img" aria-label="Photo of a dentist examining a patient" style="background:linear-gradient(135deg,#cfd9e0,#e8d3c6)"></div>
    <div class="body">
      <h3>Meet the Dentists</h3>
      <p>Meet the team that knows both chairside care and the books behind it.</p>
      <span class="go"><svg width="16" height="16" viewBox="0 0 16 16"><path d="M6 4l4 4-4 4" fill="none" stroke="#fff" stroke-width="1.8"/></svg></span>
    </div>
  </article>
  <article class="hero-card" style="top:185px">
    <div class="thumb" role="img" aria-label="Photo of a dental treatment room" style="background:linear-gradient(135deg,#d7dde0,#b9c4c9)"></div>
    <div class="body">
      <h3>Dental Centre</h3>
      <p>A full view of how a modern practice runs, from front desk to ledger.</p>
      <span class="go"><svg width="16" height="16" viewBox="0 0 16 16"><path d="M6 4l4 4-4 4" fill="none" stroke="#fff" stroke-width="1.8"/></svg></span>
    </div>
  </article>
  <article class="hero-card" style="top:319px">
    <div class="thumb" role="img" aria-label="Illustration of dental implants in a gum model" style="background:linear-gradient(135deg,#e6a0a5,#f2e6e3)"></div>
    <div class="body">
      <h3>Dental Implants</h3>
      <p>Guidance on costly equipment and implant cases, planned with clear numbers.</p>
      <span class="go"><svg width="16" height="16" viewBox="0 0 16 16"><path d="M6 4l4 4-4 4" fill="none" stroke="#fff" stroke-width="1.8"/></svg></span>
    </div>
  </article>
</section>

<section class="wrap services">
  <div class="service" style="left:0;top:67px">
    <div class="icon"><svg width="46" height="46" viewBox="0 0 46 46" fill="none" stroke="#fff" stroke-width="2.5"><path d="M12 6c5 0 7 3 11 3s6-3 11-3c5 0 7 5 6 11-1 5-4 7-4 12 0 6-2 13-5 13s-3-10-8-10-5 10-8 10-5-7-5-13c0-5-3-7-4-12-1-6 1-11 6-11z"/></svg></div>
    <div class="text"><h3>Dental Implants</h3><p>Clear cost tracking for implant work, lab fees and patient plans.</p><a class="more" href="#">Read More</a></div>
  </div>
  <div class="service" style="left:508px;top:67px">
    <div class="icon"><svg width="46" height="46" viewBox="0 0 46 46" fill="none" stroke="#fff" stroke-width="2.5"><path d="M12 8c5 0 7 3 11 3s6-3 11-3c5 0 7 5 6 11-1 5-4 7-4 12 0 5-2 11-5 11s-3-9-8-9-5 9-8 9-5-6-5-11c0-5-3-7-4-12-1-6 1-11 6-11z"/><path d="M38 2v6M35 5h6M6 30v5M3.5 32.5h5"/></svg></div>
    <div class="text"><h3>Teeth Whitening</h3><p>Simple reporting for cosmetic services so you see what each visit earns.</p><a class="more" href="#">Read More</a></div>
  </div>
  <div class="service" style="left:0;top:241px">
    <div class="icon"><svg width="46" height="46" viewBox="0 0 46 46" fill="none" stroke="#fff" stroke-width="2.5"><path d="M10 8l6 4 7-5 7 5 6-4v12c0 5-4 6-4 12 0 5-2 10-5 10s-2-8-4-8-1 8-4 8-5-5-5-10c0-6-4-7-4-12z"/></svg></div>
    <div class="text"><h3>Dental Crowns</h3><p>Crown and bridge case costs kept tidy, with lab bills matched each month.</p><a class="more" href="#">Read More</a></div>
  </div>
  <div class="service" style="left:508px;top:241px">
    <div class="icon"><svg width="46" height="46" viewBox="0 0 46 46" fill="none" stroke="#fff" stroke-width="2.5"><circle cx="27" cy="18" r="11"/><path d="M19 26L7 38"/><path d="M4 10c2 0 3 1 4 1s2-1 4-1 2 2 2 4-2 3-2 6-1 4-2 4-1-3-2-3-1 3-2 3-2-2-2-4-2-4-2-6 1-4 2-4z"/></svg></div>
    <div class="text"><h3>Other Services</h3><p>Payroll, supplies and overhead reviewed so every chair stays profitable.</p><a class="more" href="#">Read More</a></div>
  </div>
  <div class="cta">
    <p>Your caring family Dental Practice in the community</p>
    <a class="button">BOOK AN APPOINTMENT</a>
  </div>
</section>

<section class="finance">
  <div class="backdrop" role="img" aria-label="Faded photo of a dentist treating a patient behind a blue tint"></div>
  <h2>BrightLedger Ltd. Financial Services</h2>
  <ul class="col-a">
    <li>Bank account and credit card reconciliations</li>
    <li>Business and personal taxes</li>
    <li>Tax planning</li>
    <li>Bill paying</li>
    <li>Bookkeeping</li>
    <li>Cash flow management</li>
  </ul>
  <ul class="col-b">
    <li>Cash or accrual basis financials (monthly, quarterly, etc.)</li>
    <li>Chart of accounts cleanup</li>
    <li>Comparison to industry averages</li>
    <li>Data entry</li>
    <li>Financial statements</li>
    <li>High-level supervision for data entry clerks</li>
  </ul>
</section>

<section class="wrap smiles">
  <h2>We are working for your perfect smile!</h2>
  <div class="smile" style="left:0;top:110px">
    <div class="photo" role="img" aria-label="Photo of a smiling woman holding a green apple" style="background:linear-gradient(135deg,#e9d3c4,#c9b29a)"></div>
    <p>Friendly care for every patient, backed by steady and careful bookkeeping.</p>
  </div>
  <div class="smile" style="left:284px;top:110px">
    <div class="photo" role="img" aria-label="Close-up photo of a bright white smile" style="background:linear-gradient(135deg,#f4f4f4,#e6c9bd)"></div>
    <p>Bright smiles and balanced books, reviewed by people who know dentistry.</p>
  </div>
  <div class="smile" style="left:0;top:368px">
    <div class="photo" role="img" aria-label="Photo of a smiling blonde woman" style="background:linear-gradient(135deg,#e8cfa8,#f0dccb)"></div>
    <p>We handle the numbers so your team can focus on each patient.</p>
  </div>
  <div class="smile" style="left:284px;top:368px">
    <div class="photo" role="img" aria-label="Photo of a smiling young woman" style="background:linear-gradient(135deg,#f2f2f2,#d9b8a2)"></div>
    <p>Monthly statements that are easy to read and ready when you need them.</p>
  </div>

  <form class="appointment">
    <header>
      <h3>Make an Appointment</h3>
      <div class="phone"><svg width="18" height="18" viewBox="0 0 24 24"><circle cx="12" cy="12" r="12" fill="#fff"/><path d="M8.5 6.5l2 2.5-1.2 1.5c.8 1.7 2.1 3 3.8 3.8l1.5-1.2 2.5 2-1.2 2c-4.6-.4-8.4-4.2-8.8-8.8z" fill="#2aa7e1"/></svg>555-014-2290</div>
    </header>
    <div class="field" style="top:124px">NAME</div>
    <div class="field" style="top:180px">EMAIL</div>
    <div class="field" style="top:236px">PHONE</div>
    <div class="field" style="top:292px">ADDRESS</div>
    <div class="field" style="top:342px;height:107px">MESSAGE</div>
    <div class="submit">SUBMIT</div>
  </form>
</section>

<footer class="site-footer">
  <div class="contact">
    <h4>Contact BrightLedger Ltd.</h4>
    <p>Phone: 555-014-2290</p>
    <p>Email: info@brightledgerltd.com</p>
  </div>
  <div class="divider" style="left:430px"></div>
  <div class="footer-brand">BrightLedger<br>Dental</div>
  <div class="divider" style="left:688px"></div>
  <div class="social"><span></span><span></span><span></span><span></span></div>
  <p class="copyright">Copyright © 2015 BrightLedger Ltd. All Rights Reserved.</p>
</footer>

</body>
</html>
```